International Food Company needs packaging design for new products

We have a logo for our new business. It is attached. Now we need a packaging design for the products that we will be selling. We are an international wholesale foods company selling foods and herbs that will be certified organic and Non-GMO imported from West Africa. We are just in the process of launching new products. We're looking for a design that is fresh and modern.

Here is a list of items that we are requesting packaging design for.

Baobob Powder-8 oz and 12 oz
Dried Mango- 8 oz
Mango Powder 8 oz and 12 oz

```html
<!DOCTYPE html>
<html lang="en">
<head>
<meta charset="utf-8">
<title>Mango Powder Label</title>
<link rel="stylesheet" href="https://fonts.googleapis.com/css2?family=Lato:wght@300;400&family=Kaushan+Script&family=Montserrat:wght@400&display=swap">
<style>
  :root {
    --backdrop: #e9e9e9;
    --label-white: #ffffff;
    --forest: #0b6b37;
    --script-green: #0f6a34;
    --brand-green: #2fae6e;
    --brand-orange: #ef8a23;
    --splash-yellow: #ffd21a;
    --splash-orange: #f7a81b;
    --ink: #111111;
  }
  html, body {
    margin: 0;
    width: 1200px;
    height: 900px;
    overflow: hidden;
    background: var(--backdrop);
  }
  .label {
    position: absolute;
    left: 390px;
    top: 114px;
    width: 420px;
    height: 672px;
    background: var(--label-white);
    border-radius: 30px;
    overflow: hidden;
  }
  .top-band {
    position: absolute;
    left: 0; top: 0;
    width: 100%;
    height: 41px;
    background: var(--forest);
    color: var(--label-white);
    font-family: "Montserrat", sans-serif;
    font-size: 24px;
    letter-spacing: 13px;
    text-indent: 13px;
    text-align: center;
    line-height: 43px;
    z-index: 3;
  }
  .artwork {
    position: absolute;
    left: 0; top: 0;
    width: 420px;
    height: 672px;
  }
  .brand {
    position: absolute;
    left: 0;
    width: 424px;
    top: 185px;
    text-align: center;
    z-index: 2;
  }
  .brand-mark {
    width: 26px; height: 26px;
    border-radius: 50%;
    background: var(--brand-green);
    margin: 0 auto 18px;
  }
  .brand-name {
    font-family: "Lato", sans-serif;
    font-weight: 300;
    font-size: 32px;
    letter-spacing: 1px;
    color: var(--brand-green);
    line-height: 1;
  }
  .brand-sub {
    font-family: "Lato", sans-serif;
    font-weight: 300;
    font-size: 12px;
    letter-spacing: 3px;
    color: var(--brand-orange);
    margin-top: 2px;
    display: flex;
    align-items: center;
    justify-content: center;
    gap: 6px;
  }
  .brand-sub::before, .brand-sub::after {
    content: "";
    width: 48px;
    height: 1px;
    background: var(--brand-orange);
  }
  .product-name {
    position: absolute;
    left: 12px;
    top: 254px;
    font-family: "Kaushan Script", cursive;
    color: var(--script-green);
    font-size: 124px;
    line-height: 1;
    z-index: 2;
    transform: rotate(-6deg);
    transform-origin: left center;
  }
  .product-type {
    position: absolute;
    left: 196px;
    top: 376px;
    font-family: "Kaushan Script", cursive;
    color: var(--script-green);
    font-size: 64px;
    line-height: 1;
    z-index: 2;
    transform: rotate(-8deg);
  }
  .seal {
    position: absolute;
    left: 14px;
    top: 554px;
    width: 88px;
    height: 88px;
    border-radius: 50%;
    background: var(--forest);
    box-shadow: inset 0 0 0 4px var(--label-white), inset 0 0 0 6px var(--forest);
    z-index: 2;
  }
  .net-weight {
    position: absolute;
    right: 20px;
    top: 580px;
    font-family: "Lato", sans-serif;
    font-size: 20px;
    line-height: 1.3;
    color: var(--ink);
    text-align: right;
    z-index: 2;
  }
</style>
</head>
<body>
  <div class="label">
    <div class="top-band">100% NATURAL</div>

    <svg class="artwork" viewBox="0 0 420 672" xmlns="http://www.w3.org/2000/svg">
      <defs>
        <linearGradient id="artTone" x1="0" y1="0" x2="0.3" y2="1">
          <stop offset="0" stop-color="var(--splash-orange)"/>
          <stop offset="1" stop-color="var(--splash-yellow)"/>
        </linearGradient>
      </defs>
      <rect role="img" aria-label="Yellow and orange paint splash with mango slices, a cubed mango half and green leaves" x="0" y="46" width="420" height="600" rx="40" fill="url(#artTone)"/>
      <circle cx="212" cy="318" r="182" fill="var(--label-white)"/>
    </svg>

    <div class="brand">
      <div class="brand-mark"></div>
      <div class="brand-name">SUNMERE</div>
      <div class="brand-sub">FOODS</div>
    </div>

    <div class="product-name">Mango</div>
    <div class="product-type">Powder</div>

    <div class="seal" role="img" aria-label="Non-GMO certification badge"></div>

    <div class="net-weight">Net Wt.<br>12 oz</div>
  </div>
</body>
</html>
```